Massage Therapy and Energy Healing Practice

I am a massage therapist, Reiki energy healer, I sell herbs and oils, and also a health lifestyle coach. I need a design that is strong because I'm not a spa. I do therapeutic work, but I want a touch of the energy and spiritual healing I do as well to be included in the design. I like blue, green, or purple colors. I live in the Blue Ridge Mountains of VA and even though my practice is in the city I like my love for nature and the earth to show through. I would like a single image logo so I can use the image many places. I need a strong brand that will let others know that I combine massage therapy in a therapeutic way while keeping my touches of energy healing, nurturing, herb crafting, and mother earth loving ways.
Updates

Just some things about me:I like to hike. I live on a farm. I own horses, cows, sheep and dogs. I love nature and the energy in produces. I'm very spiritual. I don't know how these things might help or if they do, but I know that my personality might help inspire what I will find good in a design. Added Sunday, December 13, 2015

Target Market(s)

People in pain. People who need spiritual council. Need herbal medicine advice. Holistic healthcare.

Industry/Entity Type

Massage

Contact Information for Business Card

Kneadwell Studio
Lorna T. Whitcombe C.M.T, R.M.T
40519 Hollin Creek Court, Tallowdale, VA
540-718-2437

Colors
3176b5
85abd2
876aae
9bcb3c

Requirements
Must have
• Strong Branding that promotes my massage therapy practice first
Nice to have
• Something to evoke my herbal medicine, my energy healing, my spiritual side

```html
<!DOCTYPE html>
<html lang="en">
<head>
<meta charset="utf-8">
<title>Kneadwell Studio – Business Card</title>
<link rel="stylesheet" href="https://fonts.googleapis.com/css2?family=Mystery+Quest&family=Roboto:wght@400;500&display=swap">
<style>
  :root {
    --page-bg: #eceeef;
    --card-blue: #1b57a6;
    --band-green: #7dbb2c;
    --text-white: #ffffff;
    --art-deep: #06122a;
    --art-teal: #1d8fb0;
    --art-violet: #6a3d9a;
  }
  * { margin: 0; padding: 0; box-sizing: border-box; }
  html, body {
    width: 1200px;
    height: 993px;
    overflow: hidden;
    background: var(--page-bg);
  }
  .stage {
    width: 1200px;
    height: 993px;
    display: flex;
    align-items: center;
    justify-content: center;
  }
  .business-card {
    position: relative;
    width: 840px;
    height: 480px;
    background: var(--card-blue);
    box-shadow: 0 6px 24px rgba(0, 0, 0, 0.18);
    overflow: hidden;
  }
  .energy-art {
    position: absolute;
    left: 0;
    top: 0;
    width: 300px;
    height: 100%;
    background:
      radial-gradient(ellipse 55% 60% at 50% 45%, rgba(45, 170, 205, 0.85), transparent 70%),
      radial-gradient(ellipse 40% 25% at 50% 8%, rgba(150, 70, 190, 0.7), transparent 75%),
      radial-gradient(ellipse 35% 20% at 85% 80%, rgba(120, 70, 170, 0.6), transparent 75%),
      linear-gradient(180deg, var(--art-deep), #0a2346 50%, var(--art-deep));
  }
  .brand-name {
    position: absolute;
    left: 300px;
    right: 0;
    top: 48px;
    text-align: center;
    font-family: "Mystery Quest", cursive;
    font-size: 84px;
    line-height: 88px;
    color: var(--text-white);
    letter-spacing: 2px;
  }
  .name-band {
    position: absolute;
    left: 300px;
    right: 0;
    top: 238px;
    height: 46px;
    background: var(--band-green);
    display: flex;
    align-items: center;
    padding-left: 40px;
    font-family: "Mystery Quest", cursive;
    font-size: 28px;
    color: var(--text-white);
    letter-spacing: 1px;
  }
  .contact-list {
    position: absolute;
    left: 380px;
    top: 302px;
    list-style: none;
    font-family: "Roboto", sans-serif;
    font-size: 24px;
    line-height: 34px;
    color: var(--text-white);
  }
  .contact-item {
    display: flex;
    align-items: flex-start;
    gap: 12px;
    margin-bottom: 6px;
  }
  .contact-icon {
    flex: none;
    width: 26px;
    height: 26px;
    margin-top: 4px;
  }
  .address-line2 { display: block; padding-left: 70px; }
</style>
</head>
<body>
  <main class="stage">
    <section class="business-card">
      <div class="energy-art" role="img" aria-label="Illustration of a glowing human figure with coloured chakra symbols against a starry cosmic background"></div>

      <h1 class="brand-name">Kneadwell<br>Studio</h1>

      <div class="name-band">Lorna T. Whitcombe C.M.T, R.M.T</div>

      <ul class="contact-list">
        <li class="contact-item">
          <svg class="contact-icon" viewBox="0 0 26 26" aria-hidden="true">
            <circle cx="13" cy="13" r="13" fill="#ffffff"/>
            <path d="M9 7.5c.6-.4 1.3-.3 1.6.3l1.1 2c.3.5.1 1.1-.3 1.4l-.8.6c.6 1.4 1.7 2.6 3.1 3.3l.6-.8c.3-.5.9-.6 1.4-.4l2 1.1c.6.3.7 1 .3 1.6l-.8 1c-.6.7-1.6.9-2.4.5-3-1.4-5.3-3.8-6.6-6.8-.3-.8-.1-1.8.6-2.4z" fill="#1b57a6"/>
          </svg>
          <span>40519 Hollin Creek Court,<span class="address-line2">Tallowdale, VA</span></span>
        </li>
        <li class="contact-item">
          <svg class="contact-icon" viewBox="0 0 26 26" aria-hidden="true">
            <circle cx="13" cy="13" r="13" fill="#ffffff"/>
            <path d="M13 5.5a5 5 0 0 0-5 5c0 3.6 5 9.5 5 9.5s5-5.9 5-9.5a5 5 0 0 0-5-5z" fill="#1b57a6"/>
            <circle cx="13" cy="10.5" r="1.9" fill="#ffffff"/>
          </svg>
          <span>540-718-2437</span>
        </li>
      </ul>
    </section>
  </main>
</body>
</html>
```